R&T Promotions / P.L.W. Sales Business Cards

I have 2 companies that are somewhat connected, yet sell to 2 different markets.

R&T Promotions www.rotapfx.example

We are a manufacturers representative company. We handle sales and marketing of Home Theater, Home Automation, Audio & Video products for the state of Florida. We work with Designers, Architects, Technology Consultants and Electronic Integrators to design, sell and install cutting edge technology in new and existing homes, condos and commercial spaces.

P.L.W. Sales www.plwqz.example

We are a manufacturers representative company. We handle sales and marketing of automotive Audio, Electronics, Security, Navigation and Entertainment products for the state of Florida. We work with 12-volt retailers, installers and automobile customizers to design, sell, merchandise, fabricate and install cutting edge technology in cars, boats, motor coaches, etc.

We have logo's that might still be relevant, but might need a little touching up. We need a new business card design and layout for each of the 2 companies. I would like them to have a family look, but still better speak to the customer base associated with the channel.

Target Market(s)

R&T Promotions -

Design, Engineering, Construction, Technology, elegant, tasteful.

P.L.W. Sales -

More cutting edge, industrial, youth, aggressive, fun, bold.

Industry/Entity Type

Business

Requirements
Must have
• New business card layout for both companies.
Nice to have
• A family look, or relationship to the other company. Even if it's just a logo referencing the other company.

```html
<!DOCTYPE html>
<html lang="en">
<head>
<meta charset="utf-8">
<title>P.L.W. Sales / R&amp;T Promotions Business Cards</title>
<link href="https://fonts.googleapis.com/css2?family=Arimo:wght@400;700&display=swap" rel="stylesheet">
<style>
  :root {
    --backdrop: #e9e9e7;
    --card: #ffffff;
    --ink: #111111;
    --ink-soft: #333333;
    --plw-yellow: #ffe600;
    --rt-cyan: #0aa0dc;
    --rt-navy: #0d1b3a;
  }
  * { margin: 0; padding: 0; box-sizing: border-box; }
  html, body {
    width: 1200px;
    height: 1000px;
    overflow: hidden;
    background: var(--backdrop);
    font-family: "Arimo", Arial, sans-serif;
    color: var(--ink);
  }
  .card-set {
    position: relative;
    width: 1200px;
    height: 1000px;
  }
  .business-card {
    position: absolute;
    left: 320px;
    width: 560px;
    height: 345px;
    background: var(--card);
    box-shadow: 0 2px 6px rgba(0,0,0,0.12);
  }
  .card-plw { top: 125px; }
  .card-rt { top: 530px; }

  .brand-band {
    position: absolute;
    left: 0;
    top: 56px;
    width: 320px;
    height: 137px;
    display: flex;
    flex-direction: column;
    justify-content: center;
    padding-left: 40px;
  }
  .card-plw .brand-band { background: var(--plw-yellow); }
  .card-rt .brand-band { background: var(--rt-cyan); }

  .brand-name {
    font-weight: 700;
    line-height: 0.95;
    color: var(--ink);
  }
  .card-plw .brand-name .line-1 { font-size: 58px; letter-spacing: 1px; display: block; }
  .card-plw .brand-name .line-2 { font-size: 46px; letter-spacing: 3px; display: block; }
  .card-rt .brand-name { color: var(--rt-navy); }
  .card-rt .brand-name .line-1 { font-size: 62px; display: block; }
  .card-rt .brand-name .line-2 { font-size: 20px; letter-spacing: 4px; display: block; margin-top: 6px; }

  .sister-brands {
    position: absolute;
    left: 40px;
    bottom: 36px;
    display: flex;
    align-items: flex-end;
    gap: 34px;
  }
  .sister-brand {
    font-weight: 700;
    font-size: 15px;
    line-height: 1.05;
    color: var(--ink-soft);
  }
  .sister-brand small {
    display: block;
    font-size: 8px;
    letter-spacing: 1.5px;
    margin-top: 2px;
  }

  .rep-identity {
    position: absolute;
    right: 34px;
    top: 72px;
    text-align: right;
    font-weight: 700;
    font-size: 15px;
    letter-spacing: 2px;
    line-height: 1.25;
    text-transform: uppercase;
  }
  .rep-contact {
    position: absolute;
    right: 38px;
    top: 150px;
    text-align: right;
    font-size: 13px;
    line-height: 1.4;
    color: var(--ink-soft);
    font-style: normal;
  }
  .card-rt .rep-contact { top: 140px; }
</style>
</head>
<body>
<main class="card-set">

  <section class="business-card card-plw" aria-label="P.L.W. Sales business card">
    <div class="brand-band">
      <p class="brand-name"><span class="line-1">P.L.W.</span><span class="line-2">SALES</span></p>
    </div>
    <div class="sister-brands">
      <p class="sister-brand">R&amp;T<small>PROMOTIONS</small></p>
      <p class="sister-brand">K.V.N.<small>DISTRIBUTING</small></p>
    </div>
    <p class="rep-identity">Daniel Okafor<br>Rep Principle</p>
    <address class="rep-contact">
      4210 Harbor Point Way<br>
      Tampa, FL 33609<br>
      T: 800-555-0142<br>
      F: 305-555-0187<br>
      daniel@plw-rt.example<br>
      www.plw-rt.example
    </address>
  </section>

  <section class="business-card card-rt" aria-label="R&amp;T Promotions business card">
    <div class="brand-band">
      <p class="brand-name"><span class="line-1">R&amp;T</span><span class="line-2">PROMOTIONS</span></p>
    </div>
    <div class="sister-brands">
      <p class="sister-brand">P.L.W.<small>SALES</small></p>
      <p class="sister-brand">K.V.N.<small>DISTRIBUTING</small></p>
    </div>
    <p class="rep-identity">Grant Wellsley<br>Rep Principle</p>
    <address class="rep-contact">
      4210 Harbor Point Way<br>
      Tampa, FL 33609<br>
      T: 800-555-0142<br>
      M: 727-555-0163<br>
      F: 305-555-0187<br>
      grant@plw-rt.example<br>
      www.plw-rt.example
    </address>
  </section>

</main>
</body>
</html>
```